New Web Design Project

See attachments on the content and concept. Very important that the flow of the tiers stand out

Target Market(s)

Food and Beverage Manufacturing

Industry/Entity Type

Food and Beverage

Coding

Coded - Design and coding required

Number of Pages Required

3 page

Colors
0054AA
0677BA
7BADD7
CADEEF
E8F1F8

```html
<!DOCTYPE html>
<html lang="en">
<head>
<meta charset="utf-8">
<title>Northline Quality Group – SQF Consulting</title>
<link href="https://fonts.googleapis.com/css2?family=Merriweather:wght@400;700;900&family=Arimo:wght@400;700&display=swap" rel="stylesheet">
<style>
:root{
  --blue-900:#0a2a5c;
  --blue:#0054AA;
  --blue-mid:#0677BA;
  --blue-soft:#7BADD7;
  --blue-pale:#CADEEF;
  --blue-mist:#E8F1F8;
  --ink:#1d2430;
  --grey:#7a808a;
  --navy:#0d1a33;
  --white:#fff;
}
*{margin:0;padding:0;box-sizing:border-box}
html,body{width:1200px;height:4655px;overflow:hidden}
body{position:relative;background:var(--white);font-family:"Arimo",Arial,sans-serif;color:var(--ink)}
.abs{position:absolute}
.hl{color:var(--blue);font-weight:700}

/* header */
.site-header{top:0;left:0;width:1200px;height:73px;background:#fff;border-bottom:2px solid #e3e8ef;z-index:5}
.brand{left:94px;top:6px;width:294px;height:62px;background:#f6f8fb;display:flex;align-items:center;gap:10px;padding-left:14px}
.brand-dot{width:38px;height:38px;border-radius:50%;background:var(--blue);flex:none}
.brand-name{font-family:"Merriweather",serif;font-weight:700;color:var(--blue);font-size:17px;line-height:1;white-space:nowrap}
.brand-sub{font-size:9px;letter-spacing:.6px;color:var(--blue);margin-top:5px}
.nav{left:478px;top:28px;display:flex;gap:38px;font-size:14px;color:#6b7280}
.nav .active{color:var(--blue);font-weight:700;position:relative}
.nav .active::after{content:"";position:absolute;left:-4px;right:-4px;top:41px;height:3px;background:var(--blue)}
.btn{display:inline-flex;align-items:center;justify-content:center;border-radius:22px;font-weight:700;font-size:12px;letter-spacing:.3px;text-transform:uppercase}
.btn-blue{background:var(--blue-mid);color:#fff}
.btn-white{background:#fff;color:var(--ink)}
.header-cta{left:891px;top:18px;width:194px;height:40px}

/* hero */
.hero{top:73px;left:0;width:1200px;height:680px}
.hero-photo{width:100%;height:100%;background:linear-gradient(135deg,#8fa9c6 0%,#4f6f95 45%,#2e4d75 100%)}
.hero-title{top:205px;left:180px;width:840px;text-align:center;color:#fff;font-family:"Merriweather",serif;font-weight:900;font-size:53px;line-height:62px;text-shadow:0 3px 8px rgba(0,0,0,.5)}
.hero-text{top:423px;left:315px;width:570px;text-align:center;color:#fff;font-weight:700;font-size:14px;line-height:25px;text-shadow:0 1px 4px rgba(0,0,0,.6)}
.hero-btn1{top:522px;left:413px;width:196px;height:42px}
.hero-btn2{top:522px;left:626px;width:162px;height:42px}

.eyebrow{font-size:13px;font-weight:700;color:var(--blue);letter-spacing:.3px;text-transform:uppercase}
.h2{font-family:"Merriweather",serif;font-weight:400;color:var(--ink);font-size:42px;line-height:56px}

/* steps */
.steps-eyebrow{top:865px;left:0;width:1200px;text-align:center}
.steps-title{top:893px;left:0;width:1200px;text-align:center}
.step{width:230px;text-align:center}
.step svg{display:block;margin:0 auto}
.step h3{font-family:"Merriweather",serif;font-weight:400;font-size:18px;margin-top:14px;color:var(--ink)}
.step p{font-size:11.5px;line-height:20px;color:var(--grey);margin:10px auto 0;width:210px}

/* why */
.why{top:1341px;left:0;width:1200px;height:755px;background:var(--blue-mist)}
.why-eyebrow{top:1413px;left:108px}
.why-title{top:1443px;left:108px;font-size:43px;line-height:56px}
.why-text{top:1567px;left:108px;width:480px;font-size:13px;line-height:26px;color:var(--grey)}
.why-photo-frame{top:1640px;left:160px}
.feature{left:665px;width:440px}
.feature-head{display:flex;align-items:center;gap:16px;font-size:16px;color:var(--ink)}
.ic{width:46px;height:46px;border-radius:50%;background:var(--blue);display:flex;align-items:center;justify-content:center;flex:none}
.feature p{font-size:12.5px;line-height:26px;color:var(--grey);margin-top:12px}

/* services */
.svc-eyebrow{top:2215px;left:0;width:1200px;text-align:center}
.svc-title{top:2252px;left:0;width:1200px;text-align:center;line-height:56px}
.svc-text{top:2388px;left:200px;width:800px;text-align:center;font-size:15px;line-height:29px;color:#555}
.card{top:2488px;width:314px;height:310px;background:#fff;border-radius:6px;box-shadow:0 4px 14px rgba(0,40,90,.14);padding:30px 22px}
.card.selected{border:2px solid var(--blue)}
.card-head{display:flex;align-items:center;gap:14px;font-size:19px;color:var(--ink)}
.card-head .ic{width:72px;height:72px}
.card p{font-size:13px;line-height:27px;color:var(--grey);margin-top:26px}
.arrow-btn{top:2607px;width:24px;height:24px;border-radius:50%;display:flex;align-items:center;justify-content:center}

/* testimonial */
.quote-band{top:2888px;left:0;width:1200px;height:370px;background:linear-gradient(120deg,#0054AA 0%,#0a4a93 50%,#0677BA 100%)}
.quote{top:2978px;left:190px;width:820px;text-align:center;color:#fff;font-family:"Merriweather",serif;font-weight:700;font-size:24px;line-height:44px}
.quote-by{top:3138px;left:0;width:1200px;text-align:center;color:#dfe9f5;font-family:"Merriweather",serif;font-size:18px}

/* stats */
.stat{top:3345px;width:260px}
.stat b{display:block;font-family:"Merriweather",serif;color:var(--blue);font-size:36px}
.stat span{display:block;font-size:18px;color:#555;margin-top:12px}

/* cta */
.cta{top:3520px;left:112px;width:976px;height:401px;border-radius:6px;overflow:hidden;background:linear-gradient(90deg,#0054AA 0%,#1e5fa8 40%,#8eb2d6 100%)}
.cta-photo{position:absolute;right:0;top:0;width:560px;height:401px;background:linear-gradient(90deg,rgba(0,84,170,0) 0%,#a8c4e0 40%,#d5e3f1 100%)}
.cta-title{top:3584px;left:144px;font-family:"Merriweather",serif;font-weight:900;color:#fff;font-size:40px}
.cta-text{top:3650px;left:144px;width:400px;color:#fff;font-size:15.5px;line-height:29px}
.cta-btn1{top:3749px;left:140px;width:196px;height:42px}
.cta-btn2{top:3804px;left:140px;width:294px;height:42px}

/* credentials */
.cred-title{top:4015px;left:112px;font-size:42px;line-height:54px;color:var(--ink);font-weight:400}
.cred{display:flex;align-items:center;gap:26px;font-size:16px;color:var(--ink)}
.cred .ic{width:54px;height:54px}

/* footer */
.footer{top:4240px;left:0;width:1200px;height:415px}
.f-brand{top:4400px;left:112px;display:flex;gap:16px;align-items:center}
.f-brand .dot{width:68px;height:68px;border-radius:50%;background:var(--blue)}
.f-name{font-family:"Merriweather",serif;font-weight:700;color:var(--blue-mid);font-size:29px}
.f-sub{color:#fff;font-weight:700;font-size:15px;letter-spacing:.5px;margin-top:6px}
.socials{top:4514px;left:112px;display:flex;gap:9px}
.socials span{width:34px;height:34px;border-radius:50%;background:#fff;border:3px solid var(--blue)}
.f-col h4{color:#fff;font-size:22px;font-weight:700}
.f-links{list-style:none;margin-top:16px}
.f-links li{color:#fff;font-size:14px;line-height:29px}
.contact-row{display:flex;align-items:center;gap:16px;color:#fff;font-size:14px;margin-top:18px}
.copyright{top:4627px;left:0;width:1200px;text-align:center;color:#fff;font-size:11px}
</style>
</head>
<body>

<header class="abs site-header">
  <div class="abs brand">
    <span class="brand-dot"></span>
    <div><div class="brand-name">Northline Quality Group</div><div class="brand-sub">FOOD SAFETY &amp; SQF CERTIFICATION</div></div>
  </div>
  <nav class="abs nav"><span class="active">Home</span><span>Services</span><span>Benefits</span><span>Process</span><span>Contact</span></nav>
  <a class="abs btn btn-blue header-cta">Get SQF Consultation</a>
</header>

<section class="abs hero">
  <div class="hero-photo" role="img" aria-label="Food production lab with technicians in hairnets and lab coats"></div>
  <svg class="abs" style="left:0;top:520px" width="1200" height="162" viewBox="0 0 1200 162">
    <polygon points="0,42 600,162 1200,42 1200,162 0,162" fill="#fff"/>
    <polyline points="0,35 600,155 1200,35" fill="none" stroke="#0054AA" stroke-width="14"/>
  </svg>
</section>
<h1 class="abs hero-title">Hire a tech-driven SQF team that carries you across the certification finish line.</h1>
<p class="abs hero-text">At Northline Quality Group, we focus exclusively on SQF combining real plant experience with smart technology so your team can stay focused on production while we handle the path to certification and beyond.</p>
<a class="abs btn btn-blue hero-btn1">Get SQF Consultation</a>
<a class="abs btn btn-white hero-btn2">Explore Services</a>

<!-- steps -->
<div class="abs eyebrow steps-eyebrow">How It Works</div>
<h2 class="abs h2 steps-title">From <span class="hl">Discovery to Certification</span></h2>
<svg class="abs" style="left:260px;top:1040px" width="690" height="60" viewBox="0 0 690 60" fill="none" stroke="#555" stroke-width="1.6" stroke-dasharray="5 4">
  <path d="M10 45 Q70 65 140 25"/><path d="M265 40 Q330 -5 405 45"/><path d="M520 45 Q590 65 660 25"/>
</svg>
<svg class="abs" style="left:0;top:0" width="0" height="0"><defs>
  <g id="shield"><path d="M45 4 L84 20 V56 C84 80 64 96 45 104 C26 96 6 80 6 56 V20 Z" fill="#fff" stroke="#0054AA" stroke-width="5"/><circle cx="45" cy="54" r="24" fill="#E8F1F8" stroke="#7BADD7" stroke-width="2"/><circle cx="45" cy="54" r="9" fill="#0054AA"/></g>
</defs></svg>
<div class="abs step" style="left:100px;top:1020px"><svg width="90" height="108"><use href="#shield"/></svg><h3>Discovery Call</h3><p>We learn about your facility, your current systems, and where you are in the SQF journey. No pressure-just a conversation</p></div>
<div class="abs step" style="left:353px;top:1020px"><svg width="90" height="108"><use href="#shield"/></svg><h3>Gap Assessment</h3><p>We evaluate your facility against SQF requirements, identify what's missing, and give you a clear roadmap with priorities</p></div>
<div class="abs step" style="left:608px;top:1020px"><svg width="90" height="108"><use href="#shield"/></svg><h3>Build &amp; Implement</h3><p>We design your SQF program and build it directly into your digital food safety platform forms, logs. SOPs HACCP plans, all of it</p></div>
<div class="abs step" style="left:863px;top:1020px"><svg width="90" height="108"><use href="#shield"/></svg><h3>Coach &amp; Certify</h3><p>We learn about your facility, your current systems, and where you are in the SQF journey. No pressure-just a conversation</p></div>

<!-- why -->
<section class="abs why"></section>
<div class="abs eyebrow why-eyebrow">Why Northline Quality</div>
<h2 class="abs h2 why-title">Built for <span class="hl">Small &amp;<br>Mid-Size Manufacturers</span></h2>
<p class="abs why-text">You don't need to hire a full-time food safety director or figure out SQF alone. We bring the expertise and technology you stay focused on production.</p>
<svg class="abs why-photo-frame" width="345" height="410" viewBox="0 0 345 410">
  <path d="M172 8 L336 92 V250 C336 330 260 385 172 402 C84 385 8 330 8 250 V92 Z" fill="#fff" stroke="#0054AA" stroke-width="14"/>
  <defs><linearGradient id="pg" x1="0" y1="0" x2="1" y2="1"><stop offset="0" stop-color="#c9d6e4"/><stop offset="1" stop-color="#5d7fa6"/></linearGradient></defs>
  <circle cx="172" cy="210" r="145" fill="url(#pg)" role="img" aria-label="Manager reviewing food safety data on a tablet"/>
</svg>

<div class="abs feature" style="top:1410px"><div class="feature-head"><span class="ic"><svg width="20" height="20"><circle cx="10" cy="10" r="8" fill="none" stroke="#fff" stroke-width="2"/></svg></span>Lower Cost Than a Full-Time Hire</div><p>Get a complete SQF team program design, digital implementation and coaching at a fraction of the cost of hiring a full-time SQF Practitioner</p></div>
<div class="abs feature" style="top:1560px"><div class="feature-head"><span class="ic"><svg width="20" height="20"><rect x="3" y="4" width="14" height="11" rx="1" fill="none" stroke="#fff" stroke-width="2"/></svg></span>Your Program Lives in Software</div><p>No more binders and spreadsheets. Your SQF system is built into Quorvia.io or Tellarin.io organized, accessible, and always audit-ready</p></div>
<div class="abs feature" style="top:1724px"><div class="feature-head"><span class="ic"><svg width="20" height="20"><circle cx="10" cy="10" r="7" fill="none" stroke="#fff" stroke-width="2" stroke-dasharray="3 2"/></svg></span>Flexible, Low-Risk Engagement</div><p>Start with a 3-month commitment, then go month-to-month. Cancel anytime with 30 days notice. We earn your business every month</p></div>
<div class="abs feature" style="top:1870px"><div class="feature-head"><span class="ic"><svg width="20" height="20"><path d="M4 16 L16 4" stroke="#fff" stroke-width="3"/></svg></span>Bilingual Floor-Level Support</div><p>With our Central America team, we provide training and documentation in Spanish so every member of your production team Go to understands and follows the program</p></div>

<!-- services -->
<div class="abs eyebrow svc-eyebrow">What We Do</div>
<h2 class="abs h2 svc-title">SQF Consulting, <span class="hl">Implementation<br>&amp; Onboarding</span></h2>
<p class="abs svc-text">We help food and beverage manufacturers achieve and maintain SQF certification with confidence, using practical programs and digital tools that work on the floor — not just on audit day.</p>
<div class="abs arrow-btn" style="left:35px;background:var(--blue)"><svg width="10" height="10"><path d="M7 1 L3 5 L7 9" fill="none" stroke="#fff" stroke-width="2"/></svg></div>
<div class="abs arrow-btn" style="left:1132px;background:#d0d3d8"><svg width="10" height="10"><path d="M3 1 L7 5 L3 9" fill="none" stroke="#fff" stroke-width="2"/></svg></div>
<article class="abs card" style="left:112px"><div class="card-head"><span class="ic"><svg width="30" height="30"><path d="M15 5 L26 12 L15 19 L4 12 Z" fill="none" stroke="#fff" stroke-width="2"/><path d="M4 18 L15 25 L26 18" fill="none" stroke="#fff" stroke-width="2"/></svg></span>SQF Program Design</div><p>We design your complete SQF system from scratch — HACCP/food safety plans, prerequisite programs, SOPs, forms, logs, and all required documentation tailored to your facility.</p></article>
<article class="abs card selected" style="left:441px"><div class="card-head"><span class="ic"><svg width="30" height="30"><rect x="4" y="6" width="22" height="16" rx="2" fill="none" stroke="#fff" stroke-width="2"/><path d="M11 26 H19" stroke="#fff" stroke-width="2"/></svg></span>Digital Platform Build</div><p>We build your SQF program directly into modern food safety software like Quorvia.io or Tellarin.io — digitizing forms, checklists, monitoring logs, and workflows so your team runs paperless.</p></article>
<article class="abs card" style="left:770px"><div class="card-head"><span class="ic"><svg width="30" height="30"><circle cx="15" cy="9" r="4" fill="#fff"/><path d="M6 24 C8 16 22 16 24 24" fill="none" stroke="#fff" stroke-width="2"/></svg></span>Coaching &amp; Support</div><p>After building your system, we coach your team to own and maintain it day-to-day. You run the program; we provide ongoing expert guidance so you stay audit-ready at all times.</p></article>

<!-- testimonial -->
<section class="abs quote-band" role="img" aria-label="Blue-toned production facility background"></section>
<blockquote class="abs quote">"Northline Quality Group didn't just hand us a binder. They built our entire SQF system into software and coached our team until we owned it. We passed our first audit with confidence."</blockquote>
<div class="abs quote-by">-SQF-Certified Manufacturing Client</div>

<!-- stats -->
<div class="abs stat" style="left:108px"><b>15+</b><span>Clients Onboarded</span></div>
<div class="abs stat" style="left:380px"><b>100%</b><span>Clients Onboarded</span></div>
<div class="abs stat" style="left:650px"><b>Digital</b><span>Platform Built Programs</span></div>
<div class="abs stat" style="left:925px"><b>US</b><span>Nationwide Coverage</span></div>

<!-- cta -->
<section class="abs cta"><div class="cta-photo" role="img" aria-label="Two food safety technicians reviewing a clipboard"></div></section>
<h2 class="abs cta-title">Ready to Talk SQF?</h2>
<p class="abs cta-text">Share a few details about your facility and where you are in the SQF journey. We'll follow up with a brief discovery call and a clear next step.</p>
<a class="abs btn btn-blue cta-btn1">Get SQF Consultation</a>
<a class="abs btn btn-white cta-btn2">Visit Manufacturing Intelligence</a>

<!-- credentials -->
<h2 class="abs cred-title">SQF-Certified<br><span class="hl">Manufacturing<br>Client</span></h2>
<div class="abs cred" style="left:556px;top:4013px"><span class="ic"><svg width="22" height="22"><path d="M4 12 L9 17 L18 5" fill="none" stroke="#fff" stroke-width="2.4"/></svg></span>SQF Practitioner</div>
<div class="abs cred" style="left:830px;top:4013px"><span class="ic"><svg width="22" height="22"><path d="M17 3 H5 L12 11 L5 19 H17" fill="none" stroke="#fff" stroke-width="2.4"/></svg></span>Six Sigma Black Belt</div>
<div class="abs cred" style="left:556px;top:4091px"><span class="ic"><svg width="22" height="22"><rect x="2" y="4" width="18" height="12" rx="2" fill="none" stroke="#fff" stroke-width="2"/></svg></span>Remote &amp; On-Site</div>
<div class="abs cred" style="left:830px;top:4091px"><span class="ic"><svg width="22" height="22"><circle cx="11" cy="11" r="8" fill="none" stroke="#fff" stroke-width="2"/><circle cx="11" cy="11" r="3" fill="#fff"/></svg></span>Digital-First</div>

<!-- footer -->
<footer class="abs footer">
  <svg width="1200" height="415" viewBox="0 0 1200 415">
    <polygon points="0,135 600,0 1200,135 1200,415 0,415" fill="#0d1a33"/>
    <polyline points="0,140 600,5 1200,140" fill="none" stroke="#0054AA" stroke-width="12"/>
  </svg>
</footer>
<div class="abs f-brand"><span class="dot"></span><div><div class="f-name">Northline Quality Group</div><div class="f-sub">FOOD SAFETY &amp; SQF CERTIFICATION</div></div></div>
<div class="abs socials"><span></span><span></span><span></span><span></span></div>
<div class="abs f-col" style="left:600px;top:4412px"><h4>Quick Links</h4><ul class="f-links"><li>Home</li><li>Services</li><li>Benefits</li><li>Process</li><li>Contact</li></ul></div>
<div class="abs f-col" style="left:848px;top:4412px"><h4>Contact Info</h4>
  <div class="contact-row"><svg width="20" height="20"><path d="M10 19 C4 12 3 9 3 7 A7 7 0 0 1 17 7 C17 9 16 12 10 19Z" fill="#fff"/><circle cx="10" cy="7" r="2.5" fill="#0d1a33"/></svg>Lorem Ipsum,USA -437916</div>
  <div class="contact-row" style="margin-top:26px"><svg width="20" height="20"><circle cx="10" cy="10" r="9" fill="#fff"/><path d="M6 6 L8 5 L9 8 L8 9 C9 11 10 12 11 12 L12 11 L15 12 L14 14 C9 14 6 11 6 6Z" fill="#0d1a33"/></svg>+1 888 888 8888</div>
  <div class="contact-row" style="margin-top:26px"><svg width="20" height="20"><circle cx="10" cy="10" r="9" fill="#fff"/><rect x="5" y="7" width="10" height="7" fill="none" stroke="#0d1a33" stroke-width="1.4"/></svg>info@northlinequality.com</div>
</div>
<div class="abs copyright">©2026 Northline Quality Group.All Rights Reserved</div>

</body>
</html>
```